Flyer Design

I'm looking for a new flyer design to help promote our landscape company, and some of our main service for the up and coming season. We're trying to position ourselves as a leader in our market, so obviously quality is important to us.

Our current promotion is 25% off the first month with signup of annual service.

Phone Number: (816) 555-0193
Website: gardelvista.com
Our tagline: "Your hands are full... Let us help"

The call to action: direct them to our website for a detailed list of services and to receive a free quote.

You're welcome to add your own wording and punctuation. If I like the design I will provide feedback accordingly.

I have attached a jpg of our logo to help with design colors. I will provide the vector file upon completion of this project.

Also, I've attached a few photos that I had on hand of our companies work that may help with the design. Obviously I don't want to use them all, but there are a couple just to help out. I'm not opposed to stock photos either.
Thanks

Target Market(s)

We market to high end customers, generally with home between $500k-$2mil, or household income over $200k. Quality and creativity are most important to us.

Industry/Entity Type

Landscape

Requirements
Must have
• Creativity, easy to read, modern style.

```html
<!DOCTYPE html>
<html lang="en">
<head>
<meta charset="utf-8">
<title>Gardel Vista – Flyer</title>
<link href="https://fonts.googleapis.com/css2?family=Gelasio:wght@400;700&family=Open+Sans:wght@400;700&display=swap" rel="stylesheet">
<style>
  :root {
    --page-bg: #ece7df;
    --orange: #fc5309;
    --orange-deep: #e84a06;
    --white: #ffffff;
    --ink: #1b1b1b;
    --green-band: rgba(62, 122, 18, 0.78);
    --green-light: #b9d98a;
    --green-mid: #7fb945;
    --green-dark: #4a8a1e;
    --ground: #8f8a72;
    --divider: #e3e3e3;
  }
  * { margin: 0; padding: 0; box-sizing: border-box; }
  html, body { width: 1200px; height: 1000px; overflow: hidden; background: var(--page-bg); }
  .canvas { position: relative; width: 1200px; height: 1000px; }
  .flyer {
    position: absolute; left: 50px; top: 77px;
    width: 992px; height: 762px;
    transform: scale(1.109); transform-origin: top left;
    background: var(--white);
    font-family: "Gelasio", Georgia, serif;
    overflow: hidden;
  }
  .hero {
    position: absolute; left: 0; top: 0; width: 992px; height: 653px;
    background:
      radial-gradient(ellipse 260px 200px at 180px 60px, rgba(255,255,240,0.95), rgba(255,255,240,0) 70%),
      radial-gradient(ellipse 420px 260px at 560px 380px, rgba(190,225,120,0.9), rgba(190,225,120,0) 70%),
      linear-gradient(180deg, var(--green-light) 0%, var(--green-mid) 45%, var(--green-dark) 72%, var(--ground) 90%, #7c7663 100%);
  }
  .tagline-band {
    position: absolute; left: 440px; top: 32px; width: 552px; height: 153px;
    background: linear-gradient(90deg, rgba(62,122,18,0) 0%, var(--green-band) 28%, var(--green-band) 100%);
  }
  .tagline {
    position: absolute; left: 470px; top: 72px; width: 500px;
    color: var(--white); font-weight: 700; font-size: 36px; line-height: 40px; text-align: center;
  }
  .brand {
    position: absolute; left: 40px; top: 88px;
    display: flex; align-items: center; gap: 12px;
  }
  .brand-dot { width: 34px; height: 34px; border-radius: 50%; background: var(--orange); }
  .brand-name { color: var(--white); font-weight: 700; font-size: 36px; line-height: 1; }
  .services { position: absolute; left: 0; top: 227px; }
  .service {
    display: block; height: 60px; margin-bottom: 6px;
    background: var(--orange); color: var(--white);
    font-size: 40px; line-height: 60px; padding-left: 35px;
  }
  .service--lawn { width: 600px; }
  .service--weed { width: 336px; }
  .service--hedge { width: 393px; margin-top: 2px; }
  .cta {
    position: absolute; left: 38px; top: 470px;
    color: var(--white); font-size: 40px; line-height: 43px;
  }
  .cta strong { font-weight: 700; }
  .offer-badge { position: absolute; left: 695px; top: 333px; width: 168px; height: 168px; }
  .offer-badge-text {
    position: absolute; left: 695px; top: 383px; width: 168px; text-align: center;
    color: var(--white); font-family: "Open Sans", Arial, sans-serif; line-height: 36px;
  }
  .offer-badge-text .pct { font-weight: 700; font-size: 30px; display: block; }
  .offer-badge-text .off { font-weight: 400; font-size: 34px; display: block; }
  .offer-detail {
    position: absolute; left: 618px; top: 519px; width: 320px; text-align: center;
    color: var(--white); font-weight: 700; font-size: 22px; line-height: 28px;
  }
  .footer { position: absolute; left: 0; top: 653px; width: 992px; height: 109px; background: var(--white); }
  .footer-divider { position: absolute; left: 540px; top: 20px; width: 1px; height: 70px; background: var(--divider); }
  .contact {
    position: absolute; top: 34px; display: flex; align-items: center; gap: 14px;
    color: var(--orange); font-size: 33px; line-height: 40px;
  }
  .contact--web { left: 50px; }
  .contact--phone { left: 612px; }
  .contact svg { display: block; }
</style>
</head>
<body>
<div class="canvas">
  <div class="flyer">
    <div class="hero" role="img" aria-label="Soft-focus photograph of a sunlit green garden with foliage and a stone path"></div>

    <div class="brand">
      <span class="brand-dot"></span>
      <span class="brand-name">Gardel Vista</span>
    </div>

    <div class="tagline-band"></div>
    <p class="tagline">“ Your hands are full…<br>Let us help ”</p>

    <div class="services">
      <span class="service service--lawn">Lawn care and maintenance</span>
      <span class="service service--weed">Weed control</span>
      <span class="service service--hedge">Hedge trimming</span>
    </div>

    <p class="cta"><strong>Visit</strong> or <strong>call us</strong> for<br>a detailed list of services<br>and a free quote.</p>

    <svg class="offer-badge" viewBox="0 0 168 168" aria-hidden="true">
      <polygon fill="#fc5309" points="
        84,0 90,8 97,1 102,10 110,4 114,13 123,9 125,19 134,16 135,26 144,25 143,34 152,35 149,44 158,47 153,55 161,60 155,67 162,73 155,79 160,86 153,91 157,99 149,103 152,112 143,114 144,123 135,123 134,133 125,131 122,140 114,136 110,145 102,139 97,148 90,141 84,149
        78,141 71,148 66,139 58,145 54,136 46,140 43,131 34,133 33,123 24,123 25,114 16,112 19,103 11,99 15,91 8,86 13,79 6,73 13,67 7,60 15,55 10,47 19,44 16,35 25,34 24,25 33,26 34,16 43,19 45,9 54,13 58,4 66,10 71,1 78,8" transform="translate(0,10)"/>
      <circle cx="84" cy="84" r="62" fill="none" stroke="#ffffff" stroke-width="1.5" opacity="0.8"/>
    </svg>
    <p class="offer-badge-text"><span class="pct">25%</span><span class="off">OFF</span></p>

    <p class="offer-detail">25% off the first<br>month with signup of<br>annual service</p>

    <div class="footer">
      <div class="contact contact--web">
        <svg width="46" height="32" viewBox="0 0 46 32" aria-hidden="true">
          <rect x="6" y="2" width="34" height="22" rx="1.5" fill="none" stroke="#1b1b1b" stroke-width="3"/>
          <rect x="1" y="26" width="44" height="4" rx="1" fill="#1b1b1b"/>
        </svg>
        <span>www.gardelvista.com</span>
      </div>
      <div class="footer-divider"></div>
      <div class="contact contact--phone">
        <svg width="26" height="40" viewBox="0 0 26 40" aria-hidden="true">
          <rect x="2" y="2" width="22" height="36" rx="4" fill="none" stroke="#1b1b1b" stroke-width="3"/>
          <line x1="2" y1="8" x2="24" y2="8" stroke="#1b1b1b" stroke-width="2"/>
          <line x1="2" y1="31" x2="24" y2="31" stroke="#1b1b1b" stroke-width="2"/>
          <circle cx="13" cy="34.5" r="1.6" fill="#1b1b1b"/>
        </svg>
        <span>(816) 555-0193</span>
      </div>
    </div>
  </div>
</div>
</body>
</html>
```